Roadside building business signage for a holistic health clinic.

Replace signs as shown in the attached file. They are perforated stickers that go on the windows as shown. Looking for something that has our logo and says the name of the practice with logo (Fernbrook Health & Wellness) also boldly says Acupuncture, IV Vitamins, and Holistic Health.
Possibly our phone number as well 318-627-5194
Updates

Please don't use pink except the logo. Earthy, organic tone colors appreciated.

Need of eye catching window signage of a holistic clinic on a brick building. Pink, purple, sage green, white color. Logo is pink on a white background. Please don't overload with too much pink. Words to include are "Fernbrook Health and Wellness(name of business)", "Direct Primary Care", " Medical acupuncture", "IV Vitamin Therapy", "fernbrookcare-example.com","318-627-5194".

Target Market(s)

People will see in their cars passing by the building. Busy roadside so need to be visible while passing in fast speed.

Industry/Entity Type

Health & Wellness

Font styles to use
Sans Serif

Colors

Designer to choose colors to be used in the design.

Requirements
Must have
• On sign must have words Holistic Medicine, Medical Acupuncture, Direct Primary Care and IV vitamins.
Nice to have
• Simple, minimalistic, artistic yet has clear message. White, Black, Violet, Pink (logo), Dark green, Sage green.
Should not have
• Bold colors (red, yellow, blue), same tone colors. Blue waves on the current signage (uploaded file) must go.

```html
<!DOCTYPE html>
<html lang="en">
<head>
<meta charset="utf-8">
<title>Fernbrook Health &amp; Wellness – Window Signage</title>
<link href="https://fonts.googleapis.com/css2?family=Alegreya+Sans:wght@500;800&display=swap" rel="stylesheet">
<style>
  :root {
    --backdrop: #cccccc;
    --forest: #0f4d40;
    --cream: #f9f6e8;
    --cream-line: #f3eccb;
    --white: #ffffff;
    --blossom: #d9468f;
    --skin-light: #f3e6dc;
    --skin-mid: #d7ae93;
    --skin-deep: #b9856a;
    --hair: #8a5a3c;
    --water: #cfe4ef;
    --citrus: #f2a93b;
    --leaf: #7fb24a;
    --berry: #d8433f;
    --studio: #efece7;
    --plum: #6e2a3a;
  }
  * { margin: 0; padding: 0; box-sizing: border-box; }
  html, body { width: 1200px; height: 686px; overflow: hidden; background: var(--backdrop); }
  .canvas { position: relative; width: 1200px; height: 686px; font-family: "Alegreya Sans", sans-serif; }

  .arch { position: absolute; top: 52px; width: 166px; height: 183px; }
  .arch--left { left: 419px; }
  .arch--right { left: 606px; }

  .tile { position: absolute; width: 166px; height: 182px; overflow: hidden; }
  .tile--cream { top: 252px; background: var(--cream); }
  .service-title {
    position: absolute; left: 13px; top: 30px;
    color: var(--forest); font-weight: 800; font-size: 23.5px; line-height: 22px; letter-spacing: 0.3px;
  }
  .accent-bar { position: absolute; left: 13px; bottom: 14px; width: 33px; height: 5px; background: var(--forest); }

  .brand { position: absolute; left: 0; right: 0; text-align: center; color: var(--forest); font-weight: 800; }
  .brand-dot { display: block; margin: 0 auto 10px; border-radius: 50%; background: var(--blossom); }
  .brand-name { display: block; }
  .brand-sub { display: block; font-weight: 500; }
  .brand--large { top: 48px; }
  .brand--large .brand-dot { width: 38px; height: 38px; }
  .brand--large .brand-name { font-size: 19px; line-height: 22px; letter-spacing: 2.4px; }
  .brand--large .brand-sub { font-size: 7.5px; line-height: 10px; letter-spacing: 2px; }
  .brand--small { top: 99px; }
  .brand--small .brand-dot { width: 24px; height: 24px; margin-bottom: 8px; }
  .brand--small .brand-name { font-size: 13px; line-height: 14px; letter-spacing: 1.6px; }
  .brand--small .brand-sub { font-size: 5.5px; line-height: 8px; letter-spacing: 1.4px; }

  .tile--banner { top: 445px; height: 183px; }
  .photo { position: absolute; inset: 0; }
  .photo--needles {
    background:
      radial-gradient(ellipse 60% 45% at 40% 60%, var(--skin-mid), transparent 70%),
      radial-gradient(ellipse 50% 30% at 75% 85%, var(--skin-deep), transparent 70%),
      linear-gradient(160deg, #f7f2ef 30%, var(--skin-light) 70%, var(--skin-mid));
  }
  .photo--face {
    background:
      radial-gradient(ellipse 45% 40% at 45% 60%, #edd2bf, transparent 70%),
      radial-gradient(ellipse 35% 50% at 95% 55%, var(--hair), transparent 75%),
      linear-gradient(90deg, var(--skin-light), #e6c4ad 60%, var(--skin-deep));
  }
  .photo--fruit {
    background:
      radial-gradient(circle at 22% 70%, var(--citrus) 0, transparent 16%),
      radial-gradient(circle at 12% 58%, var(--leaf) 0, transparent 12%),
      radial-gradient(circle at 60% 62%, var(--berry) 0, transparent 12%),
      radial-gradient(circle at 52% 86%, #f4dc5a 0, transparent 12%),
      radial-gradient(circle at 84% 72%, #e86b5a 0, transparent 14%),
      linear-gradient(160deg, var(--white) 30%, var(--water) 65%, var(--white));
  }
  .photo--yoga {
    background:
      radial-gradient(ellipse 22% 18% at 42% 62%, var(--plum), transparent 75%),
      radial-gradient(ellipse 35% 15% at 42% 92%, #b8b3ad, transparent 75%),
      radial-gradient(ellipse 25% 40% at 42% 55%, #dcbca7, transparent 75%),
      linear-gradient(180deg, #f4f2ee, var(--studio) 60%, #e3e0da);
  }
  .photo--cupping {
    background:
      radial-gradient(ellipse 35% 45% at 55% 55%, #e9cdb8, transparent 70%),
      radial-gradient(ellipse 45% 25% at 70% 95%, var(--skin-mid), transparent 75%),
      linear-gradient(150deg, var(--white) 40%, #f6e9e0 70%, var(--skin-light));
  }
  .tile--banner svg { position: absolute; inset: 0; }
  .banner-title {
    position: absolute; left: 0; right: 0; top: 19px; text-align: center;
    color: var(--cream); font-weight: 800; font-size: 24px; line-height: 24px; letter-spacing: 0.3px;
  }
  .call { position: absolute; left: 13px; top: 20px; color: var(--cream); font-weight: 800; }
  .call-number { display: block; font-size: 24px; line-height: 24px; letter-spacing: 0.8px; }
  .call-label { display: block; font-size: 15px; line-height: 18px; }
</style>
</head>
<body>
<div class="canvas">

  <svg class="arch arch--left" viewBox="0 0 166 183" aria-hidden="true">
    <path d="M166 0 A166 183 0 0 0 0 183 H166 Z" fill="var(--forest)"/>
  </svg>
  <svg class="arch arch--right" viewBox="0 0 166 183" aria-hidden="true">
    <path d="M0 0 A166 183 0 0 1 166 183 H0 Z" fill="var(--forest)"/>
  </svg>

  <section class="tile tile--cream" style="left:236px">
    <div class="brand brand--large">
      <span class="brand-dot"></span>
      <span class="brand-name">FERNBROOK</span>
      <span class="brand-sub">HEALTH &amp; WELLNESS</span>
    </div>
  </section>
  <section class="tile tile--cream" style="left:424px">
    <h2 class="service-title">Holistic<br>Medicine</h2>
    <span class="accent-bar"></span>
  </section>
  <section class="tile tile--cream" style="left:607px">
    <h2 class="service-title">Medical<br>Acupuncture</h2>
  </section>
  <section class="tile tile--cream" style="left:789px">
    <h2 class="service-title">Direct<br>Primary Care</h2>
    <span class="accent-bar"></span>
  </section>

  <section class="tile tile--banner" style="left:58px">
    <div class="photo photo--needles" role="img" aria-label="Photo: hands placing acupuncture needles"></div>
    <svg viewBox="0 0 166 183" aria-hidden="true">
      <path d="M0 0 H166 V70 C150 62 130 52 100 52 C70 52 50 76 0 79 Z" fill="var(--forest)"/>
      <path d="M0 79 C50 76 70 52 100 52 C130 52 150 62 166 70" fill="none" stroke="var(--cream-line)" stroke-width="2"/>
    </svg>
  </section>

  <section class="tile tile--banner" style="left:241px; background:var(--white)">
    <svg viewBox="0 0 166 183" aria-hidden="true">
      <path d="M0 0 H166 V53 C130 52 110 60 80 74 C55 84 25 80 0 78 Z" fill="var(--forest)"/>
      <path d="M0 78 C25 80 55 84 80 74 C110 60 130 52 166 53" fill="none" stroke="var(--cream-line)" stroke-width="2"/>
    </svg>
    <div class="call"><span class="call-number">318-627-5194</span><span class="call-label">CALL US</span></div>
    <div class="brand brand--small">
      <span class="brand-dot"></span>
      <span class="brand-name">FERNBROOK</span>
      <span class="brand-sub">HEALTH &amp; WELLNESS</span>
    </div>
  </section>

  <section class="tile tile--banner" style="left:424px">
    <div class="photo photo--face" role="img" aria-label="Photo: client relaxing during a facial acupuncture treatment"></div>
    <svg viewBox="0 0 166 183" aria-hidden="true">
      <path d="M0 0 H166 V52 C140 54 118 64 90 74 C60 84 30 82 0 72 Z" fill="var(--forest)"/>
      <path d="M0 72 C30 82 60 84 90 74 C118 64 140 54 166 52" fill="none" stroke="var(--cream-line)" stroke-width="2"/>
    </svg>
    <h2 class="banner-title">Acupuncture</h2>
  </section>

  <section class="tile tile--banner" style="left:607px">
    <div class="photo photo--fruit" role="img" aria-label="Photo: fresh fruit splashing in water"></div>
    <svg viewBox="0 0 166 183" aria-hidden="true">
      <path d="M0 0 H166 V62 C145 72 120 78 90 76 C55 74 30 55 0 60 Z" fill="var(--forest)"/>
      <path d="M0 60 C30 55 55 74 90 76 C120 78 145 72 166 62" fill="none" stroke="var(--cream-line)" stroke-width="2"/>
    </svg>
    <h2 class="banner-title">IV Vitamins</h2>
  </section>

  <section class="tile tile--banner" style="left:790px">
    <div class="photo photo--yoga" role="img" aria-label="Photo: woman meditating in a bright studio"></div>
    <svg viewBox="0 0 166 183" aria-hidden="true">
      <path d="M0 0 H166 V78 C140 80 120 78 95 68 C70 58 40 52 0 55 Z" fill="var(--forest)"/>
      <path d="M0 55 C40 52 70 58 95 68 C120 78 140 80 166 78" fill="none" stroke="var(--cream-line)" stroke-width="2"/>
    </svg>
    <h2 class="banner-title">Holistic Health</h2>
  </section>

  <section class="tile tile--banner" style="left:973px">
    <div class="photo photo--cupping" role="img" aria-label="Photo: hand placing a glass cupping jar"></div>
    <svg viewBox="0 0 166 183" aria-hidden="true">
      <path d="M0 0 H166 V79 C140 78 120 66 95 56 C65 46 30 58 0 70 Z" fill="var(--forest)"/>
      <path d="M0 70 C30 58 65 46 95 56 C120 66 140 78 166 79" fill="none" stroke="var(--cream-line)" stroke-width="2"/>
    </svg>
  </section>

</div>
</body>
</html>
```